Business Card for Business consulting practice

Need a design for a consultant business card. Simple and elegant.
I need the following information on the card:
Logo: (see uploaded file)
Company name: Calmora Advisory Group
Name: Dana Weltrup
Title: Managing Director - Aerospace and Defence
Phone #: 514-268-3917
e-mail: dana.weltrup@calmora-example.com
Website: www.calmora-example.com
Tagline: Proposals Management and Capture support for complex procurements

```html
<!DOCTYPE html>
<html lang="en">
<head>
<meta charset="utf-8">
<title>Calmora Advisory Group – Business Card</title>
<link rel="stylesheet" href="https://fonts.googleapis.com/css2?family=Cinzel:wght@500;600&family=Barlow:wght@400;500;600&display=swap">
<style>
  :root {
    --stage: #e6e8ea;
    --navy: #0f2d42;
    --navy-deep: #0b2335;
    --teal-glow: #1c5a6a;
    --blue: #2a8fbf;
    --ink: #1b2a36;
    --paper: #ffffff;
  }
  * { box-sizing: border-box; margin: 0; padding: 0; }
  html, body { width: 1200px; height: 801px; overflow: hidden; }
  body {
    background: var(--stage);
    font-family: "Barlow", sans-serif;
    position: relative;
  }
  .card {
    position: absolute;
    top: 246px;
    width: 540px;
    height: 309px;
    border-radius: 14px;
    overflow: hidden;
    box-shadow: 0 6px 18px rgba(0,0,0,0.15);
  }
  /* Front */
  .card--front { left: 40px; background: var(--navy); }
  .front-pattern {
    position: absolute; inset: 0;
    background: radial-gradient(ellipse at 95% 10%, var(--teal-glow) 0%, var(--navy) 55%, var(--navy-deep) 100%);
  }
  .front-brand {
    position: absolute; left: 0; right: 0; top: 128px;
    text-align: center;
  }
  .brand-name {
    font-family: "Cinzel", serif;
    font-weight: 600;
    letter-spacing: 1.5px;
  }
  .front-brand .brand-name { color: var(--paper); font-size: 26px; }
  .front-brand .brand-rule {
    width: 300px; height: 1px; margin: 8px auto 0;
    background: var(--paper);
  }
  /* Back */
  .card--back { left: 620px; background: var(--paper); }
  .back-content { position: absolute; left: 38px; top: 40px; }
  .card--back .brand-name { color: var(--navy); font-size: 22px; }
  .rule { height: 1px; background: var(--blue); }
  .rule--brand { width: 300px; margin: 8px 0 10px; }
  .tagline { color: var(--ink); font-size: 13px; line-height: 1.3; font-weight: 500; }
  .person-name {
    font-family: "Cinzel", serif; font-weight: 500;
    color: var(--blue); font-size: 26px; letter-spacing: 1px;
    margin-top: 22px;
  }
  .person-title { color: var(--ink); font-size: 13.5px; line-height: 1.3; font-weight: 500; margin-top: 4px; }
  .rule--title { width: 190px; margin: 10px 0 10px; }
  .contact { list-style: none; font-size: 13.5px; line-height: 1.35; color: var(--ink); }
  .contact .label { color: var(--blue); font-weight: 600; }
</style>
</head>
<body>
  <section class="card card--front" aria-label="Card front">
    <div class="front-pattern" role="img" aria-label="Tonal repeating brand pattern on deep navy"></div>
    <div class="front-brand">
      <div class="brand-name">Calmora Advisory Group</div>
      <div class="brand-rule"></div>
    </div>
  </section>

  <section class="card card--back" aria-label="Card back">
    <div class="back-content">
      <div class="brand-name">Calmora Advisory Group</div>
      <div class="rule rule--brand"></div>
      <p class="tagline">Proposals Management and<br>Capture support for complex procurements</p>
      <h1 class="person-name">Dana Weltrup</h1>
      <p class="person-title">Managing Director<br>Aerospace and Defence</p>
      <div class="rule rule--title"></div>
      <ul class="contact">
        <li><span class="label">Phone:</span> 514-268-3917</li>
        <li><span class="label">E-mail:</span> dana.weltrup@calmora-example.com</li>
        <li><span class="label">Website:</span> www.calmora-example.com</li>
      </ul>
    </div>
  </section>
</body>
</html>
```